Bramwell Hockey Academy

We are are Ice Hockey Development Company that provided on-ice Hockey development services. We need a Landing Page with tabs to direct to individual program pages.
Landing Page
About Page
Winter Program Page
Spring Program Page
Summer Program Page
Team Page
Tournament Page

```html
<!DOCTYPE html>
<html lang="en">
<head>
<meta charset="utf-8">
<title>Bramwell Hockey Academy – Website Pages</title>
<link href="https://fonts.googleapis.com/css2?family=Catamaran:wght@400;600;700;800&display=swap" rel="stylesheet">
<style>
  :root {
    --green: #1f7a1f;
    --green-bright: #2c9a2c;
    --black: #000000;
    --ink: #1b1b1b;
    --white: #ffffff;
    --panel: #efefef;
    --card: #f3f3f3;
    --bg-a: #d6e4cc;
    --bg-b: #bdbb93;
    --bg-c: #7dbb8e;
  }
  * { box-sizing: border-box; margin: 0; padding: 0; }
  html, body { width: 1200px; height: 675px; overflow: hidden; }
  body {
    position: relative;
    font-family: "Catamaran", Arial, sans-serif;
    color: var(--ink);
    background: linear-gradient(135deg, var(--bg-a) 0%, var(--bg-b) 50%, var(--bg-c) 100%);
  }

  /* Brand board */
  .brand-card {
    position: absolute; left: 91px; top: 103px; width: 276px; height: 141px;
    background: var(--white);
    display: flex; align-items: center; justify-content: center;
  }
  .brand-name {
    font-weight: 800; color: var(--black); text-align: center;
    font-size: 34px; line-height: 1; letter-spacing: 0.5px;
  }

  /* Page mockups */
  .page {
    position: absolute; width: 321px; background: var(--white); overflow: hidden;
  }
  .page--landing { left: 421px; top: 68px; height: 228px; }
  .page--about { left: 775px; top: 68px; height: 228px; }
  .page--team { left: 68px; top: 351px; height: 253px; }
  .page--winter { left: 421px; top: 351px; height: 228px; }
  .page--tournaments { left: 775px; top: 346px; height: 271px; }

  .site-header { position: absolute; left: 18px; right: 13px; top: 8px; height: 17px; border-bottom: 0.6px solid var(--black); }
  .page--tournaments .site-header { left: 13px; right: 15px; height: 19px; }
  .site-brand {
    position: absolute; left: 0; top: 0;
    font-weight: 800; font-size: 4.6px; line-height: 1; color: var(--black);
  }
  .site-nav {
    position: absolute; right: 2px; bottom: 3px; display: flex; gap: 5px;
    font-size: 2.8px; font-weight: 600; letter-spacing: 0.1px; color: var(--ink); list-style: none;
  }

  .photo { position: absolute; }
  .photo--skater { left: 18px; top: 34px; width: 181px; height: 131px; background: radial-gradient(ellipse at 50% 55%, #9aa09c 0%, #dfe2e0 45%, #f4f5f5 100%); }
  .photo--skates { left: 18px; top: 34px; width: 114px; height: 131px; background: linear-gradient(180deg, #9fa9a6 0%, #dfe3e3 45%, #eef0f0 70%, #6d6f70 100%); }
  .photo--coach { left: 19px; top: 33px; width: 112px; height: 81px; background: linear-gradient(160deg, #8a8a8a 0%, #d8d8d8 45%, #2b2b2b 100%); }
  .photo--net { left: 18px; top: 33px; width: 112px; height: 81px; background: linear-gradient(100deg, #c9dbe6 0%, #eef3f6 45%, #b52b22 70%, #dfe7ec 78%, #8ea7b8 100%); }
  .photo--rink { left: 13px; top: 34px; width: 114px; height: 83px; background: linear-gradient(180deg, #3a3a3a 0%, #cfcfcf 25%, #f2f2f2 60%, #1c1c1c 78%, #101010 100%); }

  .page-title {
    position: absolute; font-weight: 800; font-size: 13.5px; line-height: 1; color: var(--black); letter-spacing: 0.2px;
  }
  .page--landing .page-title { left: 206px; top: 56px; }
  .page--about .page-title { left: 148px; top: 47px; }
  .page--team .page-title { left: 148px; top: 39px; }
  .page--winter .page-title { left: 152px; top: 39px; }
  .page--tournaments .page-title { left: 143px; top: 39px; }

  .body-copy { position: absolute; font-size: 2.8px; line-height: 1.6; color: var(--ink); }
  .page--landing .body-copy { left: 206px; top: 74px; width: 100px; }
  .page--about .body-copy { left: 148px; top: 65px; width: 150px; }
  .page--about .body-copy + .body-copy { top: 109px; }
  .page--team .body-copy { left: 148px; top: 57px; width: 155px; }
  .page--winter .body-copy { left: 152px; top: 57px; width: 152px; }
  .page--tournaments .body-copy { left: 143px; top: 57px; width: 155px; }

  .cta {
    position: absolute; width: 34px; height: 11px; background: var(--green);
    color: var(--white); font-size: 2.6px; font-weight: 600; display: flex; align-items: center; justify-content: center; letter-spacing: 0.2px;
  }
  .page--landing .cta { left: 206px; top: 130px; }
  .page--about .cta { left: 148px; top: 144px; }

  /* Cards */
  .card-row { position: absolute; display: flex; list-style: none; }
  .page--team .card-row { left: 19px; top: 123px; gap: 8px; }
  .page--tournaments .card-row { left: 13px; top: 126px; gap: 8.5px; }
  .card { background: var(--card); width: 67px; height: 83px; position: relative; text-align: center; }
  .page--tournaments .card { width: 68px; height: 84px; }
  .card-photo { position: absolute; left: 6px; top: 5px; right: 6px; height: 53px; background: radial-gradient(ellipse at 50% 55%, #6f7571 0%, #d9dcda 50%, #f0f1f0 100%); }
  .card-name { position: absolute; left: 0; right: 0; top: 63px; font-size: 4.6px; font-weight: 700; color: var(--green-bright); line-height: 1; }
  .card-role { position: absolute; left: 0; right: 0; top: 70px; font-size: 2.6px; color: var(--ink); }

  /* Season band */
  .season-band { position: absolute; left: 18px; top: 120px; width: 290px; height: 51px; background: var(--panel); }
  .season-band__start { position: absolute; inset: 0; background: var(--green); clip-path: polygon(0 0, 159px 0, 129px 100%, 0 100%); }
  .season-date {
    position: absolute; top: 8px; font-weight: 700; font-size: 13px; line-height: 1.55; letter-spacing: 0.3px;
  }
  .season-date--start { left: 16px; color: var(--white); }
  .season-date--end { left: 179px; color: var(--black); }

  /* Footer */
  .site-footer { position: absolute; left: 0; right: 0; bottom: 0; height: 45px; background: var(--black); color: var(--white); }
  .page--team .site-footer { height: 34px; }
  .page--tournaments .site-footer { height: 47px; }
  .footer-brand {
    position: absolute; left: 18px; top: 10px; width: 33px; height: 19px; background: var(--white); border-radius: 2px;
    display: flex; align-items: center; justify-content: center;
    font-weight: 800; font-size: 4px; line-height: 1; color: var(--black); text-align: center;
  }
  .page--team .footer-brand { top: 9px; left: 19px; }
  .page--tournaments .footer-brand { left: 13px; top: 10px; }
  .footer-col { position: absolute; top: 13px; font-size: 2.4px; line-height: 1.5; list-style: none; }
  .page--team .footer-col { top: 13px; }
  .footer-col__head { color: var(--green-bright); font-weight: 600; }
  .footer-col--who { left: 97px; }
  .footer-col--programs { left: 133px; }
  .footer-col--contact { left: 163px; }
  .footer-col--contact .footer-col__head { color: var(--white); }
  .page--team .footer-col--who { left: 97px; }
  .page--team .footer-col--programs { left: 133px; }
  .page--team .footer-col--contact { left: 163px; }
  .social { position: absolute; right: 18px; top: 13px; display: flex; gap: 8px; }
  .social__mark { width: 6px; height: 6px; border: 1px solid var(--white); border-radius: 1px; }
  .copyright { position: absolute; left: 0; right: 0; bottom: 6px; text-align: center; font-size: 2.4px; }
  .page--team .copyright { display: none; }
</style>
</head>
<body>

  <div class="brand-card">
    <p class="brand-name">BRAMWELL<br>HOCKEY<br>DEVELOPMENT</p>
  </div>

  <!-- Landing page -->
  <section class="page page--landing">
    <header class="site-header">
      <p class="site-brand">BRAMWELL<br>HOCKEY</p>
      <ul class="site-nav"><li>ABOUT</li><li>TEAM</li><li>WINTER PROGRAM</li><li>SPRING PROGRAM</li><li>SUMMER PROGRAM</li><li>TOURNAMENTS</li></ul>
    </header>
    <div class="photo photo--skater" role="img" aria-label="Player in a white and green jersey taking a slap shot on bright ice"></div>
    <h2 class="page-title">LOREM IPSOM</h2>
    <p class="body-copy">Bramwell Hockey Academy delivers on-ice development for skaters of every level. Our coaches build skating, puck skills and game sense through focused sessions, small groups and steady feedback. Players leave each week stronger, faster and more confident on the ice.</p>
    <span class="cta">LEARN MORE</span>
    <footer class="site-footer">
      <div class="footer-brand">BRAMWELL<br>HOCKEY</div>
      <ul class="footer-col footer-col--who"><li class="footer-col__head">WHO WE ARE</li><li>ABOUT</li><li>TEAM</li><li>TOURNAMENTS</li></ul>
      <ul class="footer-col footer-col--programs"><li class="footer-col__head">PROGRAMS</li><li>WINTER</li><li>SPRING</li><li>SUMMER</li></ul>
      <ul class="footer-col footer-col--contact"><li class="footer-col__head">CONTACT US</li></ul>
      <div class="social"><span class="social__mark"></span><span class="social__mark"></span></div>
      <p class="copyright">COPYRIGHT 2023</p>
    </footer>
  </section>

  <!-- About page -->
  <section class="page page--about">
    <header class="site-header">
      <p class="site-brand">BRAMWELL<br>HOCKEY</p>
      <ul class="site-nav"><li>ABOUT</li><li>TEAM</li><li>WINTER PROGRAM</li><li>SPRING PROGRAM</li><li>SUMMER PROGRAM</li><li>TOURNAMENTS</li></ul>
    </header>
    <div class="photo photo--skates" role="img" aria-label="Pair of worn hockey skates resting in snow with a wintry forest behind"></div>
    <h2 class="page-title">ABOUT US</h2>
    <p class="body-copy">We started as a small group of coaches who wanted better ice time for young players. Today we run year-round programs built on clear goals, honest coaching and a love of the game. Every session is planned around skill growth, safety and fun.</p>
    <p class="body-copy">Our staff includes former junior and college players with years of teaching behind them. We keep groups small so each skater gets real attention.</p>
    <span class="cta">CONTACT US</span>
    <footer class="site-footer">
      <div class="footer-brand">BRAMWELL<br>HOCKEY</div>
      <ul class="footer-col footer-col--who"><li class="footer-col__head">WHO WE ARE</li><li>ABOUT</li><li>TEAM</li><li>TOURNAMENTS</li></ul>
      <ul class="footer-col footer-col--programs"><li class="footer-col__head">PROGRAMS</li><li>WINTER</li><li>SPRING</li><li>SUMMER</li></ul>
      <ul class="footer-col footer-col--contact"><li class="footer-col__head">CONTACT US</li></ul>
      <div class="social"><span class="social__mark"></span><span class="social__mark"></span></div>
      <p class="copyright">COPYRIGHT 2023</p>
    </footer>
  </section>

  <!-- Team page -->
  <section class="page page--team">
    <header class="site-header">
      <p class="site-brand">BRAMWELL<br>HOCKEY</p>
      <ul class="site-nav"><li>ABOUT</li><li>TEAM</li><li>WINTER PROGRAM</li><li>SPRING PROGRAM</li><li>SUMMER PROGRAM</li><li>TOURNAMENTS</li></ul>
    </header>
    <div class="photo photo--coach" role="img" aria-label="Black and white shot of a coach talking to kneeling players on the ice"></div>
    <h2 class="page-title">OUR TEAM</h2>
    <p class="body-copy">Meet the coaches behind every drill. Our team brings playing and teaching experience from junior, college and pro hockey, and each coach works to help players build habits that last well beyond the rink. We train together, share plans and review progress every week.</p>
    <ul class="card-row">
      <li class="card"><div class="card-photo" role="img" aria-label="Coach portrait"></div><p class="card-name">NAME</p><p class="card-role">Title</p></li>
      <li class="card"><div class="card-photo" role="img" aria-label="Coach portrait"></div><p class="card-name">NAME</p><p class="card-role">Title</p></li>
      <li class="card"><div class="card-photo" role="img" aria-label="Coach portrait"></div><p class="card-name">NAME</p><p class="card-role">Title</p></li>
      <li class="card"><div class="card-photo" role="img" aria-label="Coach portrait"></div><p class="card-name">NAME</p><p class="card-role">Title</p></li>
    </ul>
    <footer class="site-footer">
      <div class="footer-brand">BRAMWELL<br>HOCKEY</div>
      <ul class="footer-col footer-col--who"><li class="footer-col__head">WHO WE ARE</li><li>ABOUT</li><li>TEAM</li><li>TOURNAMENTS</li></ul>
      <ul class="footer-col footer-col--programs"><li class="footer-col__head">PROGRAMS</li><li>WINTER</li><li>SPRING</li><li>SUMMER</li></ul>
      <ul class="footer-col footer-col--contact"><li class="footer-col__head">CONTACT US</li></ul>
      <div class="social"><span class="social__mark"></span><span class="social__mark"></span></div>
      <p class="copyright">COPYRIGHT 2023</p>
    </footer>
  </section>

  <!-- Winter program page -->
  <section class="page page--winter">
    <header class="site-header">
      <p class="site-brand">BRAMWELL<br>HOCKEY</p>
      <ul class="site-nav"><li>ABOUT</li><li>TEAM</li><li>WINTER PROGRAM</li><li>SPRING PROGRAM</li><li>SUMMER PROGRAM</li><li>TOURNAMENTS</li></ul>
    </header>
    <div class="photo photo--net" role="img" aria-label="Outdoor rink ice beside a red hockey net on a winter day"></div>
    <h2 class="page-title">WINTER PROGRAM</h2>
    <p class="body-copy">Our winter program runs through the heart of the season with weekly skill sessions, power skating and game-play clinics. Groups are set by age and level so every player is pushed at the right pace. Spots are limited, so register early to secure your place.</p>
    <div class="season-band">
      <div class="season-band__start"></div>
      <p class="season-date season-date--start">STARTS<br>NOV 1ST</p>
      <p class="season-date season-date--end">ENDS<br>MARCH 1ST</p>
    </div>
    <footer class="site-footer">
      <div class="footer-brand">BRAMWELL<br>HOCKEY</div>
      <ul class="footer-col footer-col--who"><li class="footer-col__head">WHO WE ARE</li><li>ABOUT</li><li>TEAM</li><li>TOURNAMENTS</li></ul>
      <ul class="footer-col footer-col--programs"><li class="footer-col__head">PROGRAMS</li><li>WINTER</li><li>SPRING</li><li>SUMMER</li></ul>
      <ul class="footer-col footer-col--contact"><li class="footer-col__head">CONTACT US</li></ul>
      <div class="social"><span class="social__mark"></span><span class="social__mark"></span></div>
      <p class="copyright">COPYRIGHT 2023</p>
    </footer>
  </section>

  <!-- Tournaments page -->
  <section class="page page--tournaments">
    <header class="site-header">
      <p class="site-brand">BRAMWELL<br>HOCKEY</p>
      <ul class="site-nav"><li>ABOUT</li><li>TEAM</li><li>WINTER PROGRAM</li><li>SPRING PROGRAM</li><li>SUMMER PROGRAM</li><li>TOURNAMENTS</li></ul>
    </header>
    <div class="photo photo--rink" role="img" aria-label="Black and white view of a game in progress from behind the players' bench"></div>
    <h2 class="page-title">TOURNAMENTS</h2>
    <p class="body-copy">We enter teams in regional tournaments throughout the year, giving players a chance to test new skills in real games. Each event is led by our coaches, who handle line-ups, travel plans and game-day prep so families can simply enjoy the hockey.</p>
    <ul class="card-row">
      <li class="card"><div class="card-photo" role="img" aria-label="Tournament action photo"></div><p class="card-name">TOURNAMENT</p><p class="card-role">DATES</p></li>
      <li class="card"><div class="card-photo" role="img" aria-label="Tournament action photo"></div><p class="card-name">TOURNAMENT</p><p class="card-role">DATES</p></li>
      <li class="card"><div class="card-photo" role="img" aria-label="Tournament action photo"></div><p class="card-name">TOURNAMENT</p><p class="card-role">DATES</p></li>
      <li class="card"><div class="card-photo" role="img" aria-label="Tournament action photo"></div><p class="card-name">TOURNAMENT</p><p class="card-role">DATES</p></li>
    </ul>
    <footer class="site-footer">
      <div class="footer-brand">BRAMWELL<br>HOCKEY</div>
      <ul class="footer-col footer-col--who"><li class="footer-col__head">WHO WE ARE</li><li>ABOUT</li><li>TEAM</li><li>TOURNAMENTS</li></ul>
      <ul class="footer-col footer-col--programs"><li class="footer-col__head">PROGRAMS</li><li>WINTER</li><li>SPRING</li><li>SUMMER</li></ul>
      <ul class="footer-col footer-col--contact"><li class="footer-col__head">CONTACT US</li></ul>
      <div class="social"><span class="social__mark"></span><span class="social__mark"></span></div>
      <p class="copyright">COPYRIGHT 2023</p>
    </footer>
  </section>

</body>
</html>
```